Build Website for Playful Brand that helps content creators build businesses

Please help me create a website for my company that helps content creators build businesses around their audience. I have attached a design and vibe that I am going for at plumfinch.io.

Open for changes, but I want to keep the colour I currently have (a light teal). Ultimately the brand is playful but should come off as a very modern elevated brand.

I am looking for a few pages including

1. Home (with clear CTA button)
A section where I can input what the company does, and some brands that we have launched

2. About Me
A simple page, that has preferably able to put a circular image of myself and then give a quick background about the company

3. Blog (can you include how blog posts will appear and it should sit nicely in the page)
This ideally is a section that will be able to link to another software so my blogs automatically flow into here or posts. But otherwise it should have sections of blocks where creators can see about topics that I post about

4. Contact (this should include a form that will allow users to contact me)
Finally a contact page where it links my socials, similar what is there, but ideally there is a form they can fill out which I can link to my inbox as well. This should be a simple page as well

Create a multi page website, including a page that will link or can link blog post

Similar to this vibe and logo - https://plumfinch.io/

Target Market(s)

Content Creators

Coding

Coded - Design and coding required

Number of Pages Required

4 page

Requirements
Must have
• Home, Contact Me (Including a place to submit an enquiry and form), Blog Post Page As well

```html
<!DOCTYPE html>
<html lang="en">
<head>
<meta charset="utf-8">
<title>Plum Finch — Helping Content Creators Build Their Own Brand</title>
<link rel="stylesheet" href="https://fonts.googleapis.com/css2?family=Lato:wght@400;700;900&display=swap">
<style>
:root{
  --mint:#86dcc3;
  --mint-soft:#9fe4cf;
  --slate:#2f4346;
  --slate-deep:#233235;
  --ink:#2b3a3c;
  --muted:#6b7678;
  --white:#ffffff;
  --field:#eef1f2;
}
*{box-sizing:border-box;margin:0;padding:0}
html,body{width:1200px;height:3468px;overflow:hidden}
body{font-family:'Lato',sans-serif;color:var(--ink);background:var(--white);position:relative}
a{color:inherit;text-decoration:none}

/* header */
.topbar{position:absolute;left:380px;top:0;width:820px;height:30px;background:var(--slate);display:flex;align-items:center;color:var(--white);font-size:12px}
.topbar .socials{display:flex;gap:8px;margin-left:22px}
.topbar .socials span{width:16px;height:16px;border-radius:50%;background:var(--white);opacity:.9}
.topbar .contact{margin-left:auto;display:flex;gap:60px;margin-right:60px}
.topbar .contact span::before{content:"";display:inline-block;width:8px;height:8px;background:var(--mint);border-radius:50%;margin-right:8px}
.nav{position:absolute;left:440px;top:30px;width:760px;height:64px;background:var(--white);display:flex;align-items:center;gap:38px;padding-left:70px;font-size:14px}
.nav .active{font-weight:700;border-bottom:2px solid var(--slate);padding-bottom:4px}
.nav .cta{margin-left:auto;margin-right:70px;background:var(--mint);padding:9px 20px;border-radius:20px;font-size:13px}
.brand-plate{position:absolute;left:0;top:0;width:440px;height:190px;background:var(--white);clip-path:polygon(0 0,100% 0,100% 50%,70% 100%,0 100%);z-index:2}
.brand{position:absolute;left:24px;top:60px;display:flex;align-items:center;gap:14px;z-index:3;font-size:34px;font-weight:700;letter-spacing:4px;color:var(--slate)}
.brand i{width:44px;height:44px;border-radius:50%;background:var(--mint)}

/* hero */
.hero{position:absolute;left:0;top:0;width:1200px;height:680px;background:linear-gradient(100deg,#1c2526 0%,#3d4a4a 35%,#8a8172 60%,#c7b9a4 80%,#e6ddd0 100%)}
.hero-copy{position:absolute;left:100px;top:290px;color:var(--white);font-weight:900;line-height:1.05}
.hero-copy .l1{font-size:62px}
.hero-copy .l2{font-size:50px}
.hero-copy .btn{display:inline-block;margin-top:36px;background:var(--white);color:var(--ink);font-size:15px;font-weight:700;padding:11px 24px;border-radius:22px}

/* about */
.about-photo{position:absolute;left:140px;top:800px;width:500px;height:480px;border-radius:44px;background:linear-gradient(135deg,#2f3b3e,#6b7a7d 50%,#b9bfbf);box-shadow:0 18px 40px rgba(0,0,0,.18)}
.about-deco{position:absolute;left:0;top:1160px;width:240px;height:220px;border-radius:40% 60% 30% 40%;background:linear-gradient(160deg,#eaf5f2,var(--mint-soft))}
.about{position:absolute;left:700px;top:890px;width:420px}
.about h2{font-size:52px;font-weight:900;letter-spacing:2px;color:var(--slate)}
.about h3{font-size:19px;font-weight:700;margin:12px 0 16px}
.about p{font-size:13px;line-height:1.75;color:var(--muted);margin-bottom:14px}
.btn-mint{display:inline-block;background:var(--mint);color:var(--ink);font-weight:700;font-size:14px;padding:11px 24px;border-radius:22px}

/* what we do */
.section-title{position:absolute;left:0;width:1200px;text-align:center;font-weight:900;font-size:48px;letter-spacing:1px}
.section-sub{position:absolute;left:0;width:1200px;text-align:center;font-size:17px;color:var(--muted)}
.service{position:absolute;top:1568px;width:310px;height:392px;background:var(--white);border-radius:30px;box-shadow:0 10px 30px rgba(0,0,0,.1);overflow:hidden}
.service .media{height:215px;background:linear-gradient(135deg,#4b5a5c,#a6b1b0 60%,#e4e6e2)}
.service h4{font-size:15px;font-weight:900;margin:30px 22px 10px}
.service p{font-size:12px;line-height:1.65;color:var(--muted);margin:0 22px}

/* brands */
.brands{position:absolute;left:0;top:2080px;width:1200px;height:380px;background:radial-gradient(circle at 50% 40%,#3a5154,var(--slate-deep))}
.brands .section-title{top:68px;color:var(--white)}
.logo-card{position:absolute;top:132px;width:185px;height:120px;background:var(--white);border-radius:18px;display:flex;align-items:center;justify-content:center;gap:10px;font-size:20px;font-weight:900;color:var(--slate)}
.logo-card i{width:26px;height:26px;border-radius:50%;background:var(--mint)}
.dots{position:absolute;top:300px;left:560px;display:flex;gap:12px}
.dots span{width:26px;height:26px;border-radius:50%;background:#8b9a9b;display:flex;align-items:center;justify-content:center}

/* contact */
.contact-band{position:absolute;left:0;top:2460px;width:1200px;height:700px;background:var(--mint)}
.contact-band .section-title{top:86px;color:var(--slate);font-size:46px}
.contact-band .section-sub{top:148px;font-style:italic;color:#3f5a58;font-size:16px}
.form-card{position:absolute;left:88px;top:200px;width:1024px;height:440px;background:var(--white);border-radius:70px 70px 70px 70px}
.field{position:absolute;left:64px;width:428px;height:56px;background:var(--field);border-radius:14px;display:flex;align-items:center;justify-content:space-between;padding:0 24px;font-size:13px;color:var(--muted)}
.field svg{width:16px;height:16px}
.message{position:absolute;left:524px;top:60px;width:440px;height:360px;background:var(--field);border-radius:14px;padding:18px 24px;font-size:13px;color:var(--muted);display:flex;justify-content:space-between}
.send{position:absolute;left:64px;top:320px;width:428px;height:56px;background:var(--slate);color:var(--white);border-radius:28px;display:flex;align-items:center;justify-content:center;font-weight:700;font-size:15px}

/* footer */
.footer{position:absolute;left:0;top:3160px;width:1200px;height:308px;text-align:center}
.footer .brand-foot{position:absolute;top:70px;left:0;width:1200px;display:flex;justify-content:center;align-items:center;gap:14px;font-size:34px;font-weight:700;letter-spacing:4px;color:var(--slate)}
.footer .brand-foot i{width:44px;height:44px;border-radius:50%;background:var(--mint)}
.footer nav{position:absolute;top:224px;left:0;width:1200px;display:flex;justify-content:center;gap:62px;font-size:13px;font-weight:700}
.footer .socials{position:absolute;top:252px;left:0;width:1200px;display:flex;justify-content:center;gap:10px}
.footer .socials span{width:18px;height:18px;border-radius:50%;background:var(--slate)}
.footer small{position:absolute;top:284px;left:0;width:1200px;font-size:11px;color:var(--muted)}
</style>
</head>
<body>

<section class="hero" role="img" aria-label="Photo of three creators gathered around a desk reviewing plans"></section>
<div class="brand-plate"></div>
<a class="brand" href="https://plumfinch.io/"><i></i>PLUM FINCH</a>

<div class="topbar">
  <div class="socials"><span></span><span></span><span></span><span></span><span></span></div>
  <div class="contact"><span>info@plumfinch.io</span><span>+1 555 010 2040</span></div>
</div>
<nav class="nav">
  <a class="active" href="#">Home</a>
  <a href="#">About Me</a>
  <a href="#">Latest Blogs</a>
  <a href="#">Get Started</a>
  <a class="cta" href="#">Contact Us</a>
</nav>

<div class="hero-copy">
  <div class="l1">HELPING</div>
  <div class="l2">CONTENT CREATORS</div>
  <div class="l2">BUILD THEIR OWN</div>
  <div class="l2">BRAND</div>
  <a class="btn" href="#">Get Started</a>
</div>

<div class="about-deco" role="img" aria-label="Playful mascot illustration peeking around the photo"></div>
<div class="about-photo" role="img" aria-label="Photo of the founder smiling at a laptop in an office"></div>
<section class="about">
  <h2>ABOUT ME</h2>
  <h3>We provide the highest level of goods and service.</h3>
  <p>I help creators turn an engaged audience into a lasting business, from the first product idea to a brand that people trust, share and come back to. Every plan is built around your voice, your pace and the community you already have.</p>
  <p>No templates, no noise. We work side by side on strategy, design and launch so your brand feels as personal as the content behind it.</p>
  <a class="btn-mint" href="#">Read More</a>
</section>

<h2 class="section-title" style="top:1440px">WHAT WE DO</h2>
<p class="section-sub" style="top:1520px">Founded in 2024, we provide the highest level of goods and service.</p>

<article class="service" style="left:112px">
  <div class="media" role="img" aria-label="Photo of a team meeting around a table"></div>
  <h4>DENOUNCING PLEASURE</h4>
  <p>We help you shape clear offers, simple funnels and a brand voice your audience already loves to follow.</p>
</article>
<article class="service" style="left:445px">
  <div class="media" role="img" aria-label="Photo of colleagues talking in a bright office"></div>
  <h4>DENOUNCING PLEASURE</h4>
  <p>We help you shape clear offers, simple funnels and a brand voice your audience already loves to follow.</p>
</article>
<article class="service" style="left:778px">
  <div class="media" role="img" aria-label="Photo of hands joined together in a team huddle"></div>
  <h4>DENOUNCING PLEASURE</h4>
  <p>We help you shape clear offers, simple funnels and a brand voice your audience already loves to follow.</p>
</article>

<section class="brands">
  <h2 class="section-title">OUR BRANDS</h2>
  <div class="logo-card" style="left:88px"><i></i>Northloom</div>
  <div class="logo-card" style="left:300px"><i></i>Quillo</div>
  <div class="logo-card" style="left:508px"><i></i>Ringlet</div>
  <div class="logo-card" style="left:712px"><i></i>Boltworks Lab</div>
  <div class="logo-card" style="left:924px"><i></i>Mockery</div>
  <div class="dots">
    <span><svg width="10" height="10" viewBox="0 0 10 10"><path d="M6.5 1.5 3 5l3.5 3.5" stroke="#fff" stroke-width="1.6" fill="none"/></svg></span>
    <span><svg width="10" height="10" viewBox="0 0 10 10"><path d="M3.5 1.5 7 5 3.5 8.5" stroke="#fff" stroke-width="1.6" fill="none"/></svg></span>
  </div>
</section>

<section class="contact-band">
  <h2 class="section-title">GET IN TOUCH WITH US</h2>
  <p class="section-sub">Ducimus qui blanditiis praesentium voluptatum deleniti atque corrupti quos dolores</p>
  <form class="form-card">
    <div class="field" style="top:60px">FullName
      <svg viewBox="0 0 16 16"><circle cx="8" cy="5" r="3" fill="#2f4346"/><path d="M2 15c0-4 12-4 12 0z" fill="#2f4346"/></svg></div>
    <div class="field" style="top:146px">Email Address
      <svg viewBox="0 0 16 16"><rect x="1" y="3" width="14" height="10" rx="1" fill="#2f4346"/><path d="M1 4l7 5 7-5" stroke="#fff" fill="none"/></svg></div>
    <div class="field" style="top:232px">Contact Number
      <svg viewBox="0 0 16 16"><path d="M3 1l3 3-2 2c1 2 3 4 5 5l2-2 3 3-2 3C6 15 1 10 1 3z" fill="#2f4346"/></svg></div>
    <div class="message">Message
      <svg width="16" height="16" viewBox="0 0 16 16"><path d="M2 14l2-5 7-7 3 3-7 7z" fill="#2f4346"/></svg></div>
    <div class="send">Send Message</div>
  </form>
</section>

<footer class="footer">
  <div class="brand-foot"><i></i>PLUM FINCH</div>
  <nav><a href="#">HOME</a><a href="#">ABOUT ME</a><a href="#">LATEST BLOGS</a><a href="#">CONTACT US</a></nav>
  <div class="socials"><span></span><span></span></div>
  <small>(C) Copyright 2024 | All Rights Reserved</small>
</footer>

</body>
</html>
```